Business Cards, Stationary, Envelopes, Email Signature for new Wellness Practice
Fernleaf Wellcraft
Business Cards, Stationary, Envelopes, Email Signature for new Wellness Practice - Massage Therapy
Creative Brief
Bright & Fun-filled
Danica Vorhees CMT
CranioSacral & Massage Therapist
31867 Orchard Ave, Suite 512 Corvale Springs, OR 97014
danica@fernleafwellcraft.example
www.fernleafwellcraft.example
CMT #57364, TOVERB #62158
Include: Tune in to Fernleaf Wellcraft on (insert icons) facebook, twitter, linkedin Mossgrove CST profile http://www.quelto.example/DanicaVorhees/ Please incorporate the attached brand image into the design. My first idea is to use the brand image as the background for the card and knock out the logo and text. Please feel free to take it from there. I love the way the logo looks knocked out. I also love the way the logo looks with the bird a different color, but it has to be used in the right context or else it looks distracting.
Give yourself time to know who you are, to become all that already are. My Next Appointments Are: Day:_____ Date:______ Time:_____ Day:_____ Date:______ Time:_____ Day:_____ Date:______ Time:_____ Day:_____ Date:______ Time:_____ Day:_____ Date:______ Time:_____ If you are not able to keep you appointment, please call, text or email at least 24 hours in advance.

```html
<!DOCTYPE html>
<html lang="en">
<head>
<meta charset="utf-8">
<title>Fernleaf Wellcraft – Business Card</title>
<link href="https://fonts.googleapis.com/css2?family=Open+Sans:wght@400;600;700&display=swap" rel="stylesheet">
<style>
  :root{
    --bg:#e9e7e3;
    --card:#ffffff;
    --blue:#1d8fd6;
    --blue-deep:#1577bb;
    --green:#2f7a3c;
    --teal:#2a8aa8;
    --ink:#3a3a3a;
    --line:#9a9a9a;
  }
  *{margin:0;padding:0;box-sizing:border-box}
  html,body{width:1200px;height:629px;overflow:hidden}
  body{background:var(--bg);font-family:'Open Sans',sans-serif;color:var(--ink);
    display:flex;align-items:center;justify-content:center;gap:60px}
  .card{width:500px;height:286px;background:var(--card);position:relative;overflow:hidden;
    box-shadow:0 6px 18px rgba(0,0,0,.18)}

  /* appointment side */
  .appointment{padding:30px 34px}
  .appointment h2{font-size:15px;font-weight:700;margin-bottom:16px}
  .field-row{display:flex;gap:22px;margin-bottom:16px;font-size:12px}
  .field{display:flex;align-items:flex-end;gap:6px;flex:1}
  .field span.rule{flex:1;border-bottom:1px solid var(--line);height:14px}
  .days{display:flex;gap:16px;margin:6px 0 28px;font-size:11px}
  .day{display:flex;align-items:center;gap:5px}
  .day i{display:inline-block;width:14px;height:14px;border:1px solid var(--ink)}
  .policy h3{font-size:12px;font-weight:700;margin-bottom:4px}
  .policy p{font-size:10.5px;line-height:1.4}

  /* front side */
  .front .waves{position:absolute;left:0;bottom:0;width:500px;height:170px}
  .brand{position:absolute;top:58px;left:0;right:0;display:flex;align-items:center;justify-content:center;gap:10px}
  .brand-dot{width:16px;height:16px;border-radius:50%;background:var(--teal)}
  .brand-name{font-size:30px;font-weight:600;color:var(--teal);letter-spacing:.5px}
  .details{position:absolute;left:30px;right:26px;bottom:22px;display:flex;justify-content:space-between;color:#fff}
  .person{font-size:10px;line-height:1.5}
  .person strong{font-size:13px;font-weight:700;display:block}
  .contact{list-style:none;font-size:10px;line-height:1.75}
  .contact li{display:flex;align-items:center;gap:6px}
  .contact svg{width:11px;height:11px;flex:none}
</style>
</head>
<body>

<section class="card appointment" aria-label="Appointment card back">
  <h2>Appointment</h2>
  <div class="field-row">
    <div class="field">Name: <span class="rule"></span></div>
    <div class="field">Date: <span class="rule"></span></div>
  </div>
  <div class="field-row">
    <div class="field">Day: <span class="rule"></span></div>
    <div class="field">Time: <span class="rule"></span></div>
  </div>
  <div class="days">
    <span class="day"><i></i>MON</span>
    <span class="day"><i></i>TUE</span>
    <span class="day"><i></i>WED</span>
    <span class="day"><i></i>THU</span>
    <span class="day"><i></i>FRI</span>
    <span class="day"><i></i>SAT</span>
  </div>
  <div class="policy">
    <h3>Cancellation Policy</h3>
    <p>We require 24 hours notice for cancelled appointments otherwise a charge may be incurred.</p>
  </div>
</section>

<section class="card front" aria-label="Business card front">
  <svg class="waves" viewBox="0 0 500 170" preserveAspectRatio="none" aria-hidden="true">
    <path d="M0 40 C140 0 300 70 500 18 L500 170 L0 170 Z" fill="var(--green)"/>
    <path d="M0 52 C150 14 300 82 500 30 L500 170 L0 170 Z" fill="var(--blue)"/>
  </svg>
  <div class="brand">
    <span class="brand-dot"></span>
    <span class="brand-name">Fernleaf Wellcraft</span>
  </div>
  <div class="details">
    <div class="person">
      <strong>Danica Vorhees CMT</strong>
      CranioSacral &amp; Massage Therapist<br><br>
      31867 Orchard Ave, Suite 512<br>
      Corvale Springs, OR 97014
    </div>
    <ul class="contact">
      <li><svg viewBox="0 0 12 12"><path d="M3 1l2 2-1 1.5c.6 1.3 1.5 2.2 2.8 2.8L8.3 6l2 2-1.3 1.8C5 9.5 2.5 7 2.2 3z" fill="#fff"/></svg>(555) 014-2273</li>
      <li><svg viewBox="0 0 12 12"><rect x="1" y="2.5" width="10" height="7" fill="none" stroke="#fff"/><path d="M1 2.5l5 4 5-4" fill="none" stroke="#fff"/></svg>danica@fernleafwellcraft.example</li>
      <li><svg viewBox="0 0 12 12"><circle cx="6" cy="6" r="4.8" fill="none" stroke="#fff"/><path d="M1.2 6h9.6M6 1.2c-2.4 3-2.4 6.6 0 9.6M6 1.2c2.4 3 2.4 6.6 0 9.6" fill="none" stroke="#fff" stroke-width=".8"/></svg>www.fernleafwellcraft.example</li>
      <li><svg viewBox="0 0 12 12"><circle cx="6" cy="6" r="5" fill="#fff"/></svg>fernleafwellcraft</li>
    </ul>
  </div>
</section>

</body>
</html>
```